Japanese Rice Food Package Label

- We are launching Japanese food products to the outdoor community.
- Made in Japan
- We will have multiple flavors of rice but want to keep the package label almost the same and only replace the flavor text (e.g., Mixed Rice, Curry Rice, etc)
- We like simple designs inspired by Japan.
- Label size: 105 mm x148 mm
- Our brand: YURATO https://yurato.co/
- Video message: https://www.clipvane.com/share/4b7e19d0a3c65f2e8d1a7b30c9e5f412

```html
<!DOCTYPE html>
<html lang="en">
<head>
<meta charset="utf-8">
<title>YURATO Mixed Rice Label</title>
<link rel="stylesheet" href="https://fonts.googleapis.com/css2?family=Montserrat:wght@300&family=Roboto:wght@400;500&display=swap">
<style>
  :root {
    --teal: #0aa696;
    --band: #aae6e1;
    --mint-soft: #dcf6f4;
    --mint-line: #cdeee8;
    --subtitle: #8ccbc0;
    --paper: #ffffff;
  }
  html, body {
    margin: 0;
    padding: 0;
    overflow: hidden;
    background: var(--paper);
  }
  .label {
    position: relative;
    width: 1200px;
    height: 851px;
    background: var(--paper);
    overflow: hidden;
  }
  .backdrop,
  .brand-mark {
    position: absolute;
    left: 0;
    top: 0;
  }
  .flavor-band {
    position: absolute;
    left: 314px;
    top: 444px;
    width: 569px;
    height: 116px;
    background: var(--band);
    display: flex;
    align-items: center;
    justify-content: center;
  }
  .flavor-name {
    margin: 0;
    font-family: "Roboto", sans-serif;
    font-weight: 400;
    font-size: 86px;
    line-height: 1;
    letter-spacing: 3px;
    color: var(--paper);
    white-space: nowrap;
  }
  .origin {
    position: absolute;
    left: 0;
    width: 1200px;
    top: 572px;
    margin: 0;
    text-align: center;
    font-family: "Montserrat", sans-serif;
    font-weight: 300;
    font-size: 39px;
    line-height: 1;
    letter-spacing: 1.5px;
    color: var(--subtitle);
  }
  .brand {
    position: absolute;
    left: 0;
    width: 1200px;
    top: 646px;
    text-align: center;
  }
  .brand-name {
    position: relative;
    display: inline-block;
    margin: 0;
    font-family: "Roboto", sans-serif;
    font-weight: 500;
    font-size: 208px;
    line-height: 1;
    color: var(--teal);
    white-space: nowrap;
  }
  .brand-reg {
    position: absolute;
    left: 100%;
    top: 20px;
    margin-left: 10px;
    font-family: "Roboto", sans-serif;
    font-weight: 400;
    font-size: 62px;
    line-height: 1;
    color: var(--teal);
  }
</style>
</head>
<body>
  <main class="label">
    <svg class="backdrop" width="1200" height="851" viewBox="0 0 1200 851" role="img" aria-label="Faint Japanese blossom pattern filling the corners of the label">
      <defs>
        <radialGradient id="field-right" cx="0.5" cy="0.45" r="0.55">
          <stop offset="0" stop-color="#dcf6f4" stop-opacity="1"/>
          <stop offset="0.75" stop-color="#dcf6f4" stop-opacity="0.9"/>
          <stop offset="1" stop-color="#dcf6f4" stop-opacity="0"/>
        </radialGradient>
        <radialGradient id="field-left" cx="0.35" cy="0.6" r="0.6">
          <stop offset="0" stop-color="#dcf6f4" stop-opacity="1"/>
          <stop offset="0.7" stop-color="#dcf6f4" stop-opacity="0.85"/>
          <stop offset="1" stop-color="#dcf6f4" stop-opacity="0"/>
        </radialGradient>
        <radialGradient id="field-faint" cx="0.3" cy="0.5" r="0.6">
          <stop offset="0" stop-color="#e9f8f5" stop-opacity="1"/>
          <stop offset="1" stop-color="#e9f8f5" stop-opacity="0"/>
        </radialGradient>
      </defs>
      <ellipse cx="1080" cy="260" rx="320" ry="330" fill="url(#field-right)"/>
      <ellipse cx="110" cy="720" rx="220" ry="210" fill="url(#field-left)"/>
      <ellipse cx="90" cy="280" rx="260" ry="280" fill="url(#field-faint)"/>
      <ellipse cx="1110" cy="800" rx="220" ry="140" fill="url(#field-faint)"/>
    </svg>

    <svg class="brand-mark" width="1200" height="851" viewBox="0 0 1200 851" aria-hidden="true">
      <circle cx="600" cy="215" r="150" fill="var(--mint-soft)" stroke="var(--teal)" stroke-width="4"/>
    </svg>

    <div class="flavor-band">
      <h1 class="flavor-name">MIXED RICE</h1>
    </div>

    <p class="origin">MADE IN JAPAN</p>

    <div class="brand">
      <p class="brand-name">YURATO<span class="brand-reg">®</span></p>
    </div>
  </main>
</body>
</html>
```